Solar Ad for direct mail campaign designed to grab attention

My company is doing a direct mail campaign on a 6.25-9in flyer. There will be wording on it, but I need a picture to grab attention. I need a picture of a pink unicorn made out of solar panels fighting a pirate ship with power lines and electrical wires on it in a battle of the galaxy scene. I want to make it look like a mystical solar creature is saving the planet from the "power pirates" AKA power company. Please be over-the-top and creative.

Target Market(s)

30-55 year old homeowners

Industry/Entity Type

Solar Energy

Font styles to use
Sans Serif

Colors
876aae
b768aa
e667a6
fece3e
33b8a4
3176b5

Requirements
Must have
• Lots of Color, exxagertion and creativity
Nice to have
• I want the unicorn to be the largest thing on the picture, with a picture of the earth in the backround. The pirate ship must be battling with the unicorn. The pirate ship must have power lines on it, and the pirates must have on yellow hard hats to show that they represent the power company
Should not have
• no rainbows

```html
<!DOCTYPE html>
<html lang="en">
<head>
<meta charset="utf-8">
<title>Save the Universe with Solar – Flyer</title>
<link href="https://fonts.googleapis.com/css2?family=Montserrat:wght@400;500;700;800&family=Oswald:wght@400&display=swap" rel="stylesheet">
<style>
  :root{
    --page:#e9e9ea;
    --space-deep:#0d1430;
    --space-mid:#1f2a55;
    --nebula-violet:#876aae;
    --nebula-pink:#b768aa;
    --nebula-rose:#e667a6;
    --nebula-teal:#33b8a4;
    --nebula-blue:#3176b5;
    --sun:#fece3e;
    --white:#ffffff;
    --soft:#e4e6f0;
    --shadow:#4a5068;
  }
  *{box-sizing:border-box;margin:0;padding:0}
  html,body{width:1200px;height:810px;overflow:hidden}
  body{background:var(--page);font-family:"Montserrat",sans-serif;position:relative}

  .flyer{position:absolute;top:24px;width:530px;height:762px;overflow:hidden;box-shadow:0 4px 14px rgba(0,0,0,.25)}
  .flyer--front{left:58px}
  .flyer--back{left:612px}

  .artwork{position:absolute;inset:0}
  .artwork--front{
    background:
      radial-gradient(ellipse 55% 45% at 65% 45%, #d9d6e0 0%, rgba(217,214,224,.55) 35%, transparent 70%),
      radial-gradient(ellipse 40% 30% at 85% 12%, rgba(230,103,166,.55), transparent 70%),
      radial-gradient(ellipse 50% 35% at 20% 25%, rgba(49,118,181,.7), transparent 70%),
      radial-gradient(ellipse 60% 30% at 50% 95%, rgba(135,106,174,.6), transparent 70%),
      linear-gradient(160deg, var(--space-mid) 0%, #4b3a6e 45%, #6a4a62 70%, var(--space-deep) 100%);
  }
  .artwork--back{
    background:
      radial-gradient(ellipse 40% 25% at 92% 8%, rgba(230,103,166,.5), transparent 70%),
      radial-gradient(ellipse 35% 25% at 8% 55%, rgba(49,118,181,.55), transparent 70%),
      radial-gradient(ellipse 30% 20% at 96% 60%, rgba(135,106,174,.55), transparent 70%),
      linear-gradient(170deg, #2a2c5a 0%, var(--space-deep) 55%, #1a1d38 100%);
  }

  .title{position:absolute;left:0;right:0;text-align:center;color:var(--white)}
  .title__top,.title__bottom{font-family:"Oswald",sans-serif;font-weight:400;letter-spacing:.42em;display:block}
  .title__main{font-family:"Montserrat",sans-serif;font-weight:800;display:block;line-height:1;
    color:var(--white);text-shadow:3px 3px 0 var(--shadow);-webkit-text-stroke:1px #c9ccd8}

  .flyer--front .title{top:560px}
  .flyer--front .title__top{font-size:29px;margin-left:.4em}
  .flyer--front .title__main{font-size:60px;letter-spacing:.02em;margin:4px 0 8px}
  .flyer--front .title__bottom{font-size:24px;margin-left:.4em}

  .panel{position:absolute;left:46px;right:46px;top:0;bottom:0;
    background:linear-gradient(180deg, rgba(14,20,48,.82), rgba(14,20,48,.7) 70%, rgba(14,20,48,.55));
    color:var(--white);text-align:center;padding:0 16px}

  .flyer--back .title{position:static;padding-top:22px}
  .flyer--back .title__top{font-size:22px;margin-left:.4em}
  .flyer--back .title__main{font-size:45px;margin:2px 0 2px}
  .flyer--back .title__bottom{font-size:18px;margin-left:.4em}

  .question{color:var(--sun);font-weight:700;line-height:1.3}
  .question--first{font-size:13.5px;margin-top:22px}
  .question--second{font-size:14.5px;margin-top:10px}
  .lead{font-size:10.5px;margin-top:5px}
  .body-copy{font-size:9.5px;line-height:1.45;margin-top:12px;padding:0 8px}

  .divider{display:block;margin:14px auto 0;width:200px;height:6px}

  .quote-source{font-size:10.5px;margin-top:12px}
  .quote-source a{color:var(--sun);text-decoration:none}
  .quote{font-size:15px;line-height:1.35;font-weight:400;padding:0 40px}

  .details{margin:8px 0 0;border:1px dashed rgba(255,255,255,.6);border-radius:10px;padding:10px 12px 14px}
  .details p{font-size:8.6px;line-height:1.45;margin-bottom:8px}
  .details .highlight{color:var(--sun);text-transform:uppercase}
  .details .cta-small{font-size:11px;margin:14px 0 4px}
  .cta-date{font-size:20px;font-weight:700;color:var(--sun);line-height:1.2}
  .cta-call{font-size:27px;font-weight:400;line-height:1.1}
  .cta-call strong{font-weight:800}
</style>
</head>
<body>

  <section class="flyer flyer--front">
    <div class="artwork artwork--front" role="img" aria-label="Galactic battle scene: a winged white unicorn made of solar panels charges spaceships firing lasers, with nebulae, planets and a glowing earth behind"></div>
    <h1 class="title">
      <span class="title__top">SAVE THE</span>
      <span class="title__main">UNIVERSE</span>
      <span class="title__bottom">WITH SOLAR!</span>
    </h1>
  </section>

  <section class="flyer flyer--back">
    <div class="artwork artwork--back" role="img" aria-label="Deep space backdrop with nebulae, meteors, spaceships and planets"></div>
    <div class="panel">
      <h2 class="title">
        <span class="title__top">SAVE THE</span>
        <span class="title__main">UNIVERSE</span>
        <span class="title__bottom">WITH SOLAR!</span>
      </h2>

      <p class="question question--first">Would you go Solar if it was cheaper than electricity?</p>
      <p class="lead">If you answered yes, KEEP READING</p>
      <p class="body-copy">Solar has become the cheaper option. Not only does it cost nothing to install, but it puts money back in your pocket day one!</p>

      <svg class="divider" viewBox="0 0 200 6" aria-hidden="true">
        <line x1="0" y1="3" x2="200" y2="3" stroke="rgba(255,255,255,.45)" stroke-width="1"/>
        <circle cx="100" cy="3" r="2.5" fill="#fff"/>
      </svg>

      <p class="question question--second">How would you like to know that you will never<br>have to worry about another price increase<br>from the power company, EVER?</p>

      <svg class="divider" viewBox="0 0 200 6" aria-hidden="true">
        <line x1="0" y1="3" x2="200" y2="3" stroke="rgba(255,255,255,.45)" stroke-width="1"/>
        <circle cx="100" cy="3" r="2.5" fill="#fff"/>
      </svg>

      <p class="quote-source">According to <a href="#">sunfactsdaily.com</a></p>
      <p class="quote">“Solar is the most abundant energy resource on earth”</p>

      <div class="details">
        <p>Here’s what we want you to do: Look up electricity rate increases from the past ten, and twenty years and ask yourself if you want to wait around for the same increases for the future...</p>
        <p>When we first began installing solar, our customers were worried that this was “too good to be true”. But after their first year of having solar, their only regret was that they didn’t call us sooner!</p>
        <p>“Solar is amazing! If you can pay for a light bill, you can pay for solar!” -Dana Whitlock</p>
        <p>Doesn’t it bother you that the power companies are going to keep increasing the price for no real reason at all? Most of all, aren’t you nauseated by the fact that you will never cease paying for your electrical bill?! Solar is that answer! <span class="highlight">No out of pocket costs, savings day one, increased property value, owning your power rather than getting the power companies richer!</span></p>
        <p class="cta-small">SEE IF YOUR HOME QUALIFIES FOR FREE!</p>
        <p class="cta-date">NOW THROUGH FRBRUARY 15TH!</p>
        <p class="cta-call">CALL NOW! <strong>XXXXXXXX</strong></p>
      </div>
    </div>
  </section>

</body>
</html>
```